Fish guide business card

Buisiness card

Target Market(s)

Visitors to Kelp Cove NL wanting to catch fish in the ocean and have a memorable adventure fun filled day

Industry/Entity Type

Tourism

Contact Information for Business Card

Phone number 250 318 two cards Ray 250 318 7262 other card Lou 250 6093714 both have email info@lwgullrocktours.com and website www.lwgullrocktours.com

Requirements
Must have
• Email, website , name , phone , logo , Kelp Cove NL
Nice to have
• Uploaded pictures have boat and man with fish picture

```html
<!DOCTYPE html>
<html lang="en">
<head>
<meta charset="utf-8">
<title>LW Gull Rock Tours – Business Card</title>
<link href="https://fonts.googleapis.com/css2?family=Montserrat:wght@600;700&display=swap" rel="stylesheet">
<style>
  :root {
    --teal: #02a9c2;
    --navy: #261f63;
    --white: #ffffff;
    --backdrop: #818286;
    --rule: #7d7d80;
  }
  html, body {
    margin: 0;
    width: 1200px;
    height: 1000px;
    overflow: hidden;
    background: var(--backdrop);
    font-family: "Montserrat", Arial, sans-serif;
  }
  .canvas { position: relative; width: 1200px; height: 1000px; }
  .card {
    position: absolute;
    left: 293px;
    width: 615px;
    height: 350px;
    overflow: hidden;
  }
  .card-front { top: 100px; background: var(--teal); }
  .card-back { top: 511px; background: var(--white); }

  .brand-mark {
    position: absolute;
    border-radius: 50%;
    background: var(--white);
    border: 5px solid var(--navy);
    box-sizing: border-box;
    display: flex;
    align-items: center;
    justify-content: center;
    text-align: center;
    color: var(--navy);
    font-weight: 700;
    line-height: 1.15;
  }
  .card-front .brand-mark {
    left: 201px; top: 69px; width: 213px; height: 213px;
    font-size: 24px;
  }
  .card-back .brand-mark {
    left: 36px; top: 25px; width: 120px; height: 120px;
    border-width: 3px;
    font-size: 14px;
  }

  .corner-swoosh { position: absolute; left: 0; top: 0; }

  .person-name {
    position: absolute;
    left: 36px; top: 197px;
    margin: 0;
    font-size: 28px;
    font-weight: 700;
    color: var(--teal);
  }
  .divider {
    position: absolute;
    left: 36px; top: 245px;
    width: 549px; height: 0;
    border-top: 2px solid var(--rule);
  }
  .contact-list, .address {
    position: absolute;
    top: 256px;
    margin: 0; padding: 0;
    list-style: none;
    font-size: 15.5px;
    font-weight: 600;
    color: var(--navy);
    line-height: 24px;
  }
  .contact-list { left: 36px; }
  .contact-list li { display: flex; align-items: center; gap: 7px; }
  .contact-list svg { width: 14px; height: 14px; flex: none; }
  .address { right: 32px; text-align: right; font-style: normal; }
</style>
</head>
<body>
<div class="canvas">

  <section class="card card-front">
    <div class="brand-mark">LW Gull<br>Rock Tours</div>
  </section>

  <section class="card card-back">
    <svg class="corner-swoosh" width="615" height="350" viewBox="0 0 615 350" aria-hidden="true">
      <path d="M382,0 C520,30 590,110 615,179 L615,0 Z" fill="var(--teal)"/>
      <path d="M543,0 C575,35 600,80 615,124 L615,0 Z" fill="var(--navy)"/>
    </svg>

    <div class="brand-mark">LW Gull<br>Rock Tours</div>

    <h1 class="person-name">Ray</h1>
    <div class="divider"></div>

    <ul class="contact-list">
      <li>
        <svg viewBox="0 0 14 14" aria-hidden="true"><rect x="3" y="0.5" width="8" height="13" rx="1.5" fill="none" stroke="var(--teal)" stroke-width="1.6"/><rect x="5.5" y="10.5" width="3" height="1.3" fill="var(--teal)"/></svg>
        250-318-7262
      </li>
      <li>
        <svg viewBox="0 0 14 14" aria-hidden="true"><rect x="0.5" y="2.5" width="13" height="9" fill="var(--teal)"/><path d="M0.5,2.5 L7,8 L13.5,2.5 M0.5,11.5 L5,7 M13.5,11.5 L9,7" fill="none" stroke="var(--white)" stroke-width="1"/></svg>
        info@lwgullrocktours.com
      </li>
      <li>
        <svg viewBox="0 0 14 14" aria-hidden="true"><g fill="none" stroke="var(--teal)" stroke-width="1.3"><circle cx="7" cy="7" r="6"/><ellipse cx="7" cy="7" rx="2.6" ry="6"/><path d="M1,7 H13 M2,4 H12 M2,10 H12"/></g></svg>
        lwgullrocktours.com
      </li>
    </ul>

    <address class="address">
      PO Box 417<br>
      Kelp Cove NL<br>
      A1K4T8, CA
    </address>
  </section>

</div>
</body>
</html>
```